Wix web design for healthcare IT consulting firm.

I am looking for a web design built in Wix that it will be easy for me to add or edit content in the future. The web site does not need to be overly complicated, but it should look very polished and professional. I also want to ensure it is mobile device friendly. I do not need any type of on-line purchasing ability. I will eventually do blogs, but for now it is a fairly standard web site with main page, about us, services provided, etc. I would also like a place for potential customers to contact us directly from the web site. I have included a Word document with some content for the web design. I have also included my logo and business card for reference. I would like to utilize similar colors as my business card. One of my primary competitors is https://vonmarlhq.example/

Target Market(s)

Target market could be nursing home CEO, CIO, or other leader at an organization that manages long term care facilities.

Number of Pages Required

5+ page

Colors
876aae

Requirements
Must have
• Be designed to be used in Wix. Use the content I provided to create and make web design. Allow to be viewed on mobile device. Please use similar color structure as attached business card. Please use attached logo in design.

```html
<!DOCTYPE html>
<html lang="en">
<head>
<meta charset="utf-8">
<title>Services | BrightPath Healthcare Solutions</title>
<link href="https://fonts.googleapis.com/css2?family=Montserrat:wght@500;700;800&family=Questrial&family=Roboto+Mono:wght@700&display=swap" rel="stylesheet">
<style>
:root{
  --purple:#7b2fb0;
  --lavender:#876aae;
  --lavender-light:#a48cc4;
  --grey:#8c8c8c;
  --grey-light:#ececec;
  --text:#555;
  --white:#fff;
  --photo-a:#dfe8ee;
  --photo-b:#b9ccd8;
}
*{margin:0;padding:0;box-sizing:border-box}
html,body{width:1200px;height:800px;overflow:hidden;background:var(--white)}
body{position:relative;font-family:"Questrial",sans-serif;color:var(--text)}
.site-header{position:absolute;left:0;top:0;width:1200px;height:40px;background:linear-gradient(90deg,var(--lavender) 0,var(--lavender) 294px,var(--lavender-light) 294px,#b9a8d2 100%)}
.brand{position:absolute;left:90px;top:4px;width:163px;height:32px;background:#6f4fa0;display:flex;align-items:center;justify-content:center;gap:6px;color:var(--white);font-family:"Montserrat",sans-serif;font-weight:700;font-size:12px}
.brand-dot{width:8px;height:8px;border-radius:50%;background:var(--white)}
.main-nav{position:absolute;left:626px;top:19px;display:flex;height:16px}
.main-nav a{display:flex;align-items:center;justify-content:center;background:#f4f4f4;color:var(--lavender);font-family:"Montserrat",sans-serif;font-weight:700;font-size:8px;letter-spacing:.5px;text-decoration:none;border-right:1px solid #ddd}
.main-nav a.active{background:var(--purple);color:var(--white)}
.page-title{position:absolute;left:0;top:44px;width:1190px;text-align:center;font-family:"Montserrat",sans-serif;font-weight:800;font-size:27px;letter-spacing:5px;color:var(--purple)}
.title-rule{position:absolute;left:550px;top:86px;width:104px;height:4px;background:var(--grey)}
.intro{position:absolute;left:197px;top:99px;width:767px;height:94px;border:3px solid var(--purple);padding:12px 14px;font-size:11px;line-height:9.6px;letter-spacing:1.05px;color:#444;white-space:nowrap;overflow:hidden}
.photo-band{position:absolute;left:0;top:213px;width:1200px;height:451px;background:linear-gradient(90deg,var(--photo-a),var(--photo-b) 30%,var(--photo-a) 50%,var(--photo-b) 70%,var(--photo-a))}
.ehr-column{position:absolute;left:437px;top:195px;width:319px;height:469px;background:var(--white);border-left:1px dashed #aaa;border-right:1px dashed #aaa}
.ehr-heading{position:absolute;left:0;top:4px;width:100%;text-align:center;font-family:"Montserrat",sans-serif;font-weight:500;font-size:8px;color:#333}
.service{position:absolute;left:7px;width:300px}
.service-image{position:absolute;left:0;top:0;width:146px;background:#d9d9d9}
.service-name{position:absolute;left:178px;top:0;font-family:"Roboto Mono",monospace;font-weight:700;font-size:9px;line-height:13px;color:var(--white)}
.service-name span{background:var(--purple);padding:0 1px;box-decoration-break:clone;-webkit-box-decoration-break:clone}
.service-desc{position:absolute;left:149px;width:140px;font-size:5.5px;line-height:8px;color:#555}
.it-heading{position:absolute;left:546px;top:632px;z-index:2;font-family:"Montserrat",sans-serif;font-weight:500;font-size:14.5px;line-height:16px;color:var(--purple)}
.it-band{position:absolute;left:0;top:664px;width:1200px;height:136px;display:flex;z-index:1}
.it-col{height:100%;display:flex;flex-direction:column;align-items:center;padding-top:22px;text-align:center}
.it-col h3{font-family:"Montserrat",sans-serif;font-weight:800;font-size:5.5px;line-height:5.5px;letter-spacing:1.5px;width:64px;margin-bottom:6px}
.it-col p{font-size:4.6px;line-height:5.8px;width:60px}
.col-risk{width:216px;background:var(--lavender);color:var(--white)}
.col-policy{width:254px;background:var(--grey);color:var(--white)}
.col-policy h3{color:var(--purple)}
.col-cio{width:252px;background:var(--grey-light);color:#333;padding-top:20px}
.col-cio h3{color:var(--purple)}
.col-ciso{width:254px;background:var(--purple);color:var(--white)}
.col-eval{width:224px;background:var(--lavender);color:var(--white)}
</style>
</head>
<body>
<header class="site-header">
  <div class="brand"><span class="brand-dot"></span>BrightPath Healthcare</div>
  <nav class="main-nav">
    <a href="#" style="width:99px">HOME</a>
    <a href="#" style="width:105px">ABOUT</a>
    <a href="#" style="width:124px">OUR TEAM</a>
    <a href="#" class="active" style="width:117px">SERVICES</a>
    <a href="#" style="width:119px">CONTACT</a>
  </nav>
</header>

<h1 class="page-title">SERVICES</h1>
<div class="title-rule"></div>

<div class="intro">We understand different organizations have different needs.&nbsp; BrightPath HCS strives to assist your<br>organization by bringing solutions that are easy to understand and allow the customer to track success.<br>We provide solutions based on the customer's needs and desires.<br>Typically, all services provided by BrightPath HCS will also include a defined deliverable.&nbsp; The purpose is the<br>ensure the value we provide to our customers can be clearly identified and defined prior to the work<br>getting started.</div>

<div class="photo-band" role="img" aria-label="Pale blue-grey photograph of a modern glass building interior"></div>

<section class="ehr-column">
  <h2 class="ehr-heading">Electronic Health Record (EHR) Services</h2>
  <div class="service" style="top:21px">
    <div class="service-image" style="height:52px" role="img" aria-label="Image for business news"></div>
    <div class="service-name" style="top:1px"><span>BUSINESS NEWS</span></div>
    <p class="service-desc" style="top:19px">Provide guidance and resources to assist with improving the effective use of the customer's EHR system.</p>
  </div>
  <div class="service" style="top:107px">
    <div class="service-image" style="height:51px" role="img" aria-label="Image for EHR implementation"></div>
    <div class="service-name" style="top:-3px"><span>EHR<br>Implementation</span></div>
    <p class="service-desc" style="top:34px">Assist or conduct a complete EHR implementation.</p>
  </div>
  <div class="service" style="top:192px">
    <div class="service-image" style="height:51px" role="img" aria-label="Image for EHR assessment"></div>
    <div class="service-name" style="top:-2px"><span>EHR Assessment</span></div>
    <p class="service-desc" style="top:13px">Provide a high-level assessment of an organization and how they are currently utilizing the system</p>
  </div>
  <div class="service" style="top:261px">
    <div class="service-image" style="height:64px" role="img" aria-label="Image for EHR quality assessment"></div>
    <div class="service-name" style="top:0"><span>EHR Quality<br>Assessment</span></div>
    <p class="service-desc" style="top:34px;line-height:9.5px">Provide a customized quality assessment to assist with improving quality indicator scores.</p>
  </div>
  <div class="service" style="top:367px">
    <div class="service-image" style="height:64px" role="img" aria-label="Image for on-going EHR support"></div>
    <div class="service-name" style="top:0"><span>On-Going EHR<br>Support</span></div>
    <p class="service-desc" style="top:34px;line-height:9.5px">Provide on-going support for an organization on a monthly fee basis</p>
  </div>
</section>

<h2 class="it-heading">Information<br>Technology<br>Services</h2>

<section class="it-band">
  <div class="it-col col-risk">
    <h3>RISK ASSESSMENT</h3>
    <p>Provide comprehensive risk assessment including identifying all risks associated with the customer's electronic protected health information (ePHI).</p>
  </div>
  <div class="it-col col-policy">
    <h3>POLICY MANAGEMENT AND CONSULTING</h3>
    <p>Provide guidance on IT policy management, particularly policies required and recommended by national Health Insurance Portability and Accountability Act (HIPAA) guidelines.</p>
  </div>
  <div class="it-col col-cio">
    <h3>CHIEF INFORMATION OFFICER (CIO) SERVICES</h3>
    <p>Act as the organization's CIO or IT Director to assist with improving departments functions and effectiveness.</p>
    <h3 style="margin-top:4px">ON-GOING CIO OR CISO SUPPORT</h3>
    <p>Provide on-going support for an organization on a monthly fee basis</p>
  </div>
  <div class="it-col col-ciso">
    <h3>CHIEF INFORMATION SECURITY OFFICER (CISO) SERVICES</h3>
    <p>Act as the organization's CIO or IT Director to assist with improving department's functions and effectiveness.</p>
  </div>
  <div class="it-col col-eval">
    <h3>IT DEPARTMENT EVALUATION</h3>
    <p>I'm a paragraph. Double click me or click Edit Text, it's easy.</p>
  </div>
</section>
</body>
</html>
```